Startup Drone Platform Company business card

We are needing a business card design for our employees. We are a startup drone platform. We are looking for a business card that has our logo on one side, with the employee/company details on the opposite side. We are looking for something that is very eye catching, modern, and bold.

Target Market(s)

This will target both drone pilots and drone businesses, along with all the industries that could utilize drone services (aerial video, aerial photos, inspections, 3d mapping, etc).

Industry/Entity Type

Business

```html
<!DOCTYPE html>
<html lang="en">
<head>
<meta charset="utf-8">
<title>Skyward Lift — Business Card</title>
<link rel="stylesheet" href="https://fonts.googleapis.com/css2?family=Titillium+Web:wght@400;600;700&display=swap">
<style>
  :root {
    --page-bg: #ecebe8;
    --card-light: #1f72bd;
    --card-mid: #1766b2;
    --card-dark: #0f58a3;
    --ink: #ffffff;
    --ink-soft: #dbe8f6;
    --accent: #4fc3e6;
    --card-w: 420px;
    --card-h: 234px;
  }
  * { box-sizing: border-box; margin: 0; padding: 0; }
  html, body {
    width: 1200px;
    height: 512px;
    overflow: hidden;
    background: var(--page-bg);
    font-family: "Titillium Web", sans-serif;
    color: var(--ink);
  }
  .canvas {
    width: 1200px;
    height: 512px;
    display: flex;
    flex-direction: column;
    align-items: center;
    justify-content: center;
    gap: 20px;
  }
  .card {
    position: relative;
    width: var(--card-w);
    height: var(--card-h);
    overflow: hidden;
    background: var(--card-dark);
  }
  .card-bg {
    position: absolute;
    inset: 0;
    width: 100%;
    height: 100%;
  }

  /* Front */
  .brand {
    position: absolute;
    right: 16px;
    bottom: 12px;
    display: flex;
    flex-direction: column;
    align-items: center;
  }
  .brand-dot {
    width: 40px;
    height: 40px;
    border-radius: 50%;
    border: 2px solid var(--ink);
    margin-bottom: 12px;
  }
  .brand-name {
    font-size: 15px;
    font-weight: 400;
    letter-spacing: 0.42em;
    margin-right: -0.42em;
    line-height: 1.1;
  }
  .brand-sub {
    font-size: 9px;
    font-weight: 400;
    letter-spacing: 0.3em;
    margin-right: -0.3em;
    line-height: 1.4;
  }

  /* Back */
  .person {
    position: absolute;
    top: 16px;
    right: 18px;
    text-align: right;
  }
  .person-name {
    font-size: 17px;
    font-weight: 600;
    line-height: 1.1;
  }
  .person-title {
    font-size: 10px;
    font-weight: 400;
    color: var(--ink-soft);
  }
  .contact {
    position: absolute;
    left: 28px;
    bottom: 12px;
    list-style: none;
    font-size: 10px;
    line-height: 1.2;
  }
  .contact-item {
    display: flex;
    align-items: center;
    gap: 5px;
    margin-top: 8px;
  }
  .contact-item:first-child { align-items: flex-start; }
  .contact-icon {
    width: 14px;
    height: 14px;
    flex: none;
    fill: var(--ink);
  }
</style>
</head>
<body>
<main class="canvas">

  <section class="card card-front" aria-label="Card front">
    <svg class="card-bg" viewBox="0 0 420 234" preserveAspectRatio="none">
      <rect width="420" height="234" fill="var(--card-light)" role="img" aria-label="Faint globe grid decoration in light blue"/>
      <path d="M0 0 L420 0 L420 90 Q260 70 0 170 Z" fill="var(--card-mid)" opacity="0.35"/>
      <circle cx="380" cy="520" r="430" fill="var(--card-dark)"/>
    </svg>
    <div class="brand">
      <span class="brand-dot"></span>
      <span class="brand-name">SKYWARD</span>
      <span class="brand-sub">LIFT</span>
    </div>
  </section>

  <section class="card card-back" aria-label="Card back">
    <svg class="card-bg" viewBox="0 0 420 234" preserveAspectRatio="none">
      <rect width="420" height="234" fill="var(--card-light)" role="img" aria-label="Faint globe grid decoration in light blue"/>
      <circle cx="40" cy="540" r="440" fill="var(--card-dark)"/>
    </svg>

    <div class="person">
      <p class="person-name">John Doe</p>
      <p class="person-title">President/CEO</p>
    </div>

    <ul class="contact">
      <li class="contact-item">
        <svg class="contact-icon" viewBox="0 0 16 16"><path d="M8 1 L1 7.5 H3 V14 H6.5 V10 H9.5 V14 H13 V7.5 H15 Z"/></svg>
        <span>Your Office<br>Address Here.</span>
      </li>
      <li class="contact-item">
        <svg class="contact-icon" viewBox="0 0 16 16"><path d="M1 3 H4 V14 H1 Z M5 2 H15 V14 H5 Z" /><rect x="7" y="4" width="6" height="2" fill="var(--card-dark)"/><rect x="7" y="8" width="6" height="1.4" fill="var(--card-dark)"/><rect x="7" y="10.5" width="6" height="1.4" fill="var(--card-dark)"/></svg>
        <span>(555) 000-000</span>
      </li>
      <li class="contact-item">
        <svg class="contact-icon" viewBox="0 0 16 16"><rect x="4" y="1" width="8" height="14" rx="1.5"/><rect x="5.5" y="3" width="5" height="5" fill="var(--card-dark)"/></svg>
        <span>(555) 000-000</span>
      </li>
      <li class="contact-item">
        <svg class="contact-icon" viewBox="0 0 16 16"><path d="M1 3 H15 V13 H1 Z"/><path d="M1.5 3.5 L8 9 L14.5 3.5" fill="none" stroke="var(--card-dark)" stroke-width="1.3"/></svg>
        <span>email@skywardlift.com</span>
      </li>
      <li class="contact-item">
        <svg class="contact-icon" viewBox="0 0 16 16"><circle cx="7.5" cy="7.5" r="6.3" fill="none" stroke="var(--ink)" stroke-width="1.3"/><ellipse cx="7.5" cy="7.5" rx="2.8" ry="6.3" fill="none" stroke="var(--ink)" stroke-width="1"/><path d="M1.2 7.5 H13.8 M2.3 4.3 H12.7 M2.3 10.7 H12.7" stroke="var(--ink)" stroke-width="1"/></svg>
        <span>www.skywardlift.com</span>
      </li>
    </ul>
  </section>

</main>
</body>
</html>
```